Postcard Design

our company name is bramwell court retreat.we provide face to face psychic tarot reading and crystal healing in a very exclusive and private clinic. we provide answers and guidance for future life event and the balance for the body and soul.we are base in 17 osgood lane in london .we want a card who say what we do as clear as possible and who is eye catching to people so when they see it want to read it this is our web site www.bramwellctretreat.co.uk you need to put number on it to call us the number ContacUs:
0208 594 3126
0771 582 3307

Industry/Entity Type

Clinic

```html
<!DOCTYPE html>
<html lang="en">
<head>
<meta charset="utf-8">
<title>Bramwell Court Retreat – Postcard</title>
<link rel="stylesheet" href="https://fonts.googleapis.com/css2?family=Cinzel:wght@400;600&family=Pinyon+Script&family=Open+Sans:wght@400;600;700&display=swap">
<style>
  :root {
    --stage: #1e1e1e;
    --purple: #8e2f8a;
    --purple-deep: #6a1f6a;
    --purple-light: #b04fa4;
    --green: #2f8a3c;
    --green-deep: #1d6a2c;
    --gold: #d9b23a;
    --gold-light: #f1d66a;
    --white: #ffffff;
    --ink: #222222;
    --grey-text: #3a3a3a;
  }
  * { box-sizing: border-box; margin: 0; padding: 0; }
  html, body { width: 1200px; height: 1200px; overflow: hidden; background: var(--stage); }
  .canvas { position: relative; width: 1200px; height: 1200px; }

  /* ---------- Back side ---------- */
  .card-back {
    position: absolute; left: 418px; top: 26px; width: 728px; height: 558px;
    background: var(--white); overflow: hidden;
  }
  .back-panel {
    position: absolute; left: 0; top: 0; width: 353px; height: 462px;
    background: linear-gradient(160deg, var(--purple-light), var(--purple) 55%, var(--purple-deep));
  }
  .back-intro {
    position: absolute; left: 12px; top: 16px; width: 200px;
    font-family: 'Open Sans', sans-serif; font-size: 14.3px; line-height: 21px;
    color: var(--white); text-align: justify;
  }
  .drop-cap {
    float: left; font-family: 'Pinyon Script', cursive; color: var(--gold);
    font-size: 98px; line-height: 80px; height: 84px; width: 82px; margin-top: 2px;
  }
  .column-divider {
    position: absolute; left: 213px; top: 0; width: 2px; height: 462px;
    background: rgba(255,255,255,0.25);
  }
  .back-photo {
    position: absolute; left: 230px; width: 112px;
    border: 3px solid var(--gold);
  }
  .back-photo--stones {
    top: 22px; height: 210px;
    background: linear-gradient(180deg, #c9b46a 0%, #6e7a2c 35%, #3a3a34 70%, #6a6a5a 100%);
  }
  .back-photo--statue {
    top: 253px; height: 190px;
    background: radial-gradient(ellipse at 50% 60%, #c99a3a 0%, #a97a2a 40%, #d9c07a 100%);
  }
  .back-footer {
    position: absolute; left: 0; top: 462px; width: 353px; height: 96px;
    background: linear-gradient(180deg, var(--green), var(--green-deep));
    border-top: 3px solid var(--gold);
    display: flex; align-items: center;
  }
  .social { width: 205px; padding-left: 12px; }
  .social-item {
    display: flex; align-items: center; gap: 8px; margin: 6px 0;
    font-family: 'Open Sans', sans-serif; font-size: 13px; color: var(--white);
  }
  .social-mark { width: 26px; height: 26px; background: #4f7fb8; flex: none; }
  .social-mark--alt { background: #5fb6d6; }
  .footer-divider { width: 1px; height: 70px; background: rgba(255,255,255,0.5); }
  .opening {
    flex: 1; text-align: center; font-family: 'Cinzel', serif; color: var(--white);
  }
  .opening-title { font-size: 16px; font-weight: 600; letter-spacing: 0.5px; }
  .opening-days { font-size: 12px; line-height: 15px; color: var(--gold-light); }
  .back-bottom-line {
    position: absolute; left: 0; bottom: 0; width: 353px; height: 4px; background: var(--gold);
  }
  .address {
    position: absolute; left: 361px; top: 20px;
    font-family: 'Open Sans', sans-serif; font-size: 13px; line-height: 17px; color: var(--ink);
  }
  .address-name { font-weight: 700; }
  .stamp-box {
    position: absolute; left: 600px; top: 10px; width: 118px; height: 116px;
    border: 1px solid #777;
  }

  /* ---------- Front side ---------- */
  .card-front {
    position: absolute; left: 64px; top: 614px; width: 729px; height: 562px;
    background: var(--white); overflow: hidden;
  }
  .front-header {
    position: absolute; left: 0; top: 12px; width: 729px; height: 74px;
    background: linear-gradient(90deg, var(--purple-deep), var(--purple) 60%, var(--purple-light));
    border-top: 2px solid var(--gold); border-bottom: 3px solid var(--gold);
  }
  .header-photo {
    position: absolute; left: 8px; top: 4px; width: 114px; height: 62px;
    background: radial-gradient(ellipse at 40% 50%, #d99a3a, #a8602a 60%, #5a3012);
  }
  .brand-name {
    position: absolute; left: 138px; top: 10px;
    font-family: 'Cinzel', serif; font-size: 25px; letter-spacing: 7.6px; color: var(--white);
  }
  .tagline {
    position: absolute; left: 138px; top: 46px;
    font-family: 'Cinzel', serif; font-size: 11px; letter-spacing: 1.5px; color: var(--gold-light);
  }
  .front-photo {
    position: absolute; left: 0; top: 89px; width: 729px; height: 380px;
    background: linear-gradient(90deg, #4a9a3a 0%, #5f8a4a 30%, #7a5a9a 60%, #8a4aa0 100%);
  }
  .service-title {
    position: absolute; left: 18px; top: 100px;
    font-family: 'Pinyon Script', cursive; font-size: 60px; line-height: 96px; color: var(--white);
  }
  .service-sub {
    position: absolute; left: 20px; top: 318px;
    font-family: 'Cinzel', serif; font-weight: 600; font-size: 35px; line-height: 42px;
    color: var(--gold-light);
  }
  .front-lower {
    position: absolute; left: 0; top: 440px; width: 729px; height: 122px;
    background: linear-gradient(90deg, #e4e4e4 0%, #f2f2f2 55%, #d8cfc6 100%);
  }
  .lower-photo {
    position: absolute; right: 0; top: 0; width: 260px; height: 122px;
    background: linear-gradient(90deg, rgba(242,242,242,0), #c9b49a 60%, #b07a4a);
  }
  .swoosh { position: absolute; left: 0; top: 360px; width: 729px; height: 110px; }
  .contact-phones {
    position: absolute; left: 20px; top: 476px;
    font-family: 'Cinzel', serif; font-size: 27px; letter-spacing: 1.5px; color: var(--grey-text);
  }
  .contact-web {
    position: absolute; left: 20px; top: 515px;
    font-family: 'Cinzel', serif; font-size: 25px; letter-spacing: 2px; color: var(--grey-text);
  }
</style>
</head>
<body>
<main class="canvas">

  <section class="card-back">
    <div class="back-panel">
      <p class="back-intro"><span class="drop-cap">T</span>he Bramwell Court Retreat is a brand new venture aimed at creating an oasis in the midst of the city by bringing the art of psychic readings and healing. Osgood Lane is a famous landmark and has a long history and tradition of treating the body and, to a lesser degree the mind. The retreat's aim is to re-ignite the curiosity for the tarot and clairvoyance reading in helping you access answers with guidance and much more.</p>
      <div class="column-divider"></div>
      <div class="back-photo back-photo--stones" role="img" aria-label="Smooth black stones engraved with body and soul beside a candle and flower"></div>
      <div class="back-photo back-photo--statue" role="img" aria-label="Golden seated meditation statue on a gold background"></div>
    </div>
    <div class="back-footer">
      <div class="social">
        <div class="social-item"><span class="social-mark"></span>Bramwell Court Retreat</div>
        <div class="social-item"><span class="social-mark social-mark--alt"></span>@bramwellctretreat</div>
      </div>
      <div class="footer-divider"></div>
      <div class="opening">
        <div class="opening-title">Opening Times:</div>
        <div class="opening-days">Monday, Wednesday,<br>Friday &amp; Saturday<br>10:30 - 19:00</div>
      </div>
      <div class="back-bottom-line"></div>
    </div>
    <address class="address" style="font-style:normal">
      <div class="address-name">BRAMWELL COURT RETREAT</div>
      <div>17 Osgood Lane</div>
      <div>London N4 2QT</div>
    </address>
    <div class="stamp-box"></div>
  </section>

  <section class="card-front">
    <header class="front-header">
      <div class="header-photo" role="img" aria-label="Warm golden meditation statue detail"></div>
      <div class="brand-name">BRAMWELL COURT RETREAT</div>
      <div class="tagline">THE PLACE TO FIND HEALING, GUIDANCE AND ANSWERS FOR YOUR FUTURE.</div>
    </header>
    <div class="front-photo" role="img" aria-label="Tarot cards spread on a purple cloth with a candle and clear crystals"></div>
    <div class="front-lower">
      <div class="lower-photo" role="img" aria-label="Row of coloured healing crystals and candles on a white cloth"></div>
    </div>
    <svg class="swoosh" viewBox="0 0 729 110" preserveAspectRatio="none" aria-hidden="true">
      <defs>
        <linearGradient id="swooshGreen" x1="0" x2="1">
          <stop offset="0" stop-color="#1d6a2c"/>
          <stop offset="1" stop-color="#3a9a3e"/>
        </linearGradient>
      </defs>
      <path d="M0 60 C180 10 420 120 729 40 L729 80 C430 130 200 60 0 110 Z" fill="url(#swooshGreen)"/>
      <path d="M0 70 C200 35 440 110 729 55" stroke="#ffffff" stroke-width="3" fill="none" opacity="0.9"/>
      <path d="M0 85 C200 55 450 120 729 70" stroke="#8fd36a" stroke-width="2" fill="none" opacity="0.8"/>
    </svg>
    <h1 class="service-title">Psychic Tarot and<br>Angel Card Reading</h1>
    <h2 class="service-sub">SPIRITUAL AND<br>CRYSTAL HEALING</h2>
    <div class="contact-phones">0208 594 3126 &nbsp;|&nbsp; 0771 582 3307</div>
    <div class="contact-web">WWW.BRAMWELLCTRETREAT.CO.UK</div>
  </section>

</main>
</body>
</html>
```